Brambleton Fish House Menu design

We are a new Seafood Restaurant in NW Montana. We will be the only one in about 200 Miles. We are a Casual/Upscale Restaurant featureing and Oyster Bar/Live Lobster Tank/ Outdoor Seating with beautiful lake views. We have huge garage doors that open up to our big outdoor patio and outdor stage for live music.
I'm interested in having our menu having the ability to add a printed page daily or weekly showing the fresh fish and Oysters that we have as well as specials which will also be represented on the chalk board.
We have 75 Bottle wine list divided by grape variatal such as: Chardonnay, Savagnion Blanc, Reisling, Champagne, Pinot Noir, Melot, Syrah, Cabernet Sauvignon, Interesting Whites and Interesting reds.
We are designing the restaurant to look more Contemporary/urban chic/industrial with reclaimed wood as well. White's Blues and Grey's are the prevolent colors.
I also have a logo we can send over.

Target Market(s)

30-65 age mainly caucasian from the Northwest region as well as tons of Canadians.

Industry/Entity Type

Restaurant

Requirements
Must have
• "Eat the Fish" is our Tagline
American and Canadian flags that are crossed
Family owned and operated

Disclaimer: All steaks and Burgers are cooked to order. "Consuming raw, undercooked and unpasteurized food items may increase your chance of foodborne illnesses." We use nut and nut based oils in some of our menu items. If you are allergic to nuts or any other foods, please let us know.

Also here is the menu: Feel free to use whatever subcatagory heading you choose this was just for us.
FINAL MENU

SMALL PLATES
1. Sweet Thai Chili Calamari
2. Shrimp Stuffed Jalapeños
3. Hamachi Crudo
4. House Smoked Salmon with Pemmick Crackers and Pickled Celery
5. Seared Teriyaki Tidbits
6. Sliders
• Crab Salad
• Sausage with Caramelized Onions, Peppers and Provolone
• Mini Cheeseburgers
7. Fried Green Tomatoes with Crab and Tarragon-Chive Aioli
8. Tomato Soup
9. Seafood Bisque
10. House Salad with Choice of Dressings
11. Small Caesar Salad

FARM
1. Caesar Salad Entrees
• Chicken
• Fish
• Crab
2. Seafood Cobb
3. Caprese
4. Farmhouse

SNACKS
1. Fish Tacos
2. Rolls
• Lobster
• Crab
• Shrimp
3. Grilled Chicken Avocado and Bacon
4. Grilled Cheese with Tomato Soup

OCEANS
1. Wood Grilled Black Smoked Sea Salt and Pepper Salmon
2. Miso Black Cod
3. Carta Fata White Fish
4. Whole Fish
5. Fish n Chips
6. Lobster
7. Steamed Clams and/or Mussels
8. Seared Scallops
9. Roasted Garlic Shrimp
10. Crab Cakes with Trio of Dipping Butters

RANCH
1. Wood Grilled 16 oz Rib Eye
2. Wood Grilled 10 oz Top Sirloin
3. Wood Grilled Half Chicken
4. Wood Grilled Pork Chop

SWEETS
1. Key Lime Pie
2. Molted Chocolate Cake
3. Banana Fosters / Cherries Jubilee

Nice to have
• We have a little bit of Hawaiian thing occuring here so you can play around with that or not.

History section would be a nice add as well.
Such as a history section of the Brambleton itself.

```html
<!DOCTYPE html>
<html lang="en">
<head>
<meta charset="utf-8">
<title>Brambleton Fish House Menu</title>
<link rel="stylesheet" href="https://fonts.googleapis.com/css2?family=Barlow+Condensed:wght@600&family=Crimson+Text:ital@0;1&family=Playfair+Display:ital@1&display=swap">
<style>
  :root {
    --blue: #0f4a8a;
    --red: #b8343a;
    --paper: #e9eaec;
    --ink: #2a2a2e;
    --note: #555559;
    --edge: #c9cacd;
    --backdrop-top: #ffffff;
    --backdrop-bottom: #f1f1f2;
    --white: #ffffff;
  }
  * { box-sizing: border-box; margin: 0; padding: 0; }
  html, body { width: 1200px; height: 681px; overflow: hidden; }
  body {
    background: linear-gradient(180deg, var(--backdrop-top), var(--backdrop-bottom));
    position: relative;
    font-family: "Crimson Text", Georgia, serif;
    color: var(--ink);
  }

  /* Cover */
  .cover {
    position: absolute; left: 33px; top: 27px; width: 445px; height: 628px;
    background: var(--paper); border: 2px solid var(--edge); border-radius: 3px;
    box-shadow: 0 2px 6px rgba(0,0,0,.12);
  }
  .cover-band {
    position: absolute; left: 0; right: 0; top: 236px; height: 155px;
    background: var(--blue); color: var(--white);
    display: flex; flex-direction: column; align-items: center; justify-content: center;
  }
  .brand-name {
    font-family: "Crimson Text", Georgia, serif; font-weight: 400;
    color: var(--white); text-align: center; line-height: 1;
  }
  .cover .brand-name { font-size: 30px; }
  .brand-sub { display: block; font-size: 14px; letter-spacing: 3px; margin-top: 4px; text-transform: uppercase; }
  .cover-label {
    font-family: "Playfair Display", Georgia, serif; font-style: italic;
    font-size: 24px; margin-top: 16px;
  }

  /* Inner spread */
  .spread {
    position: absolute; left: 548px; top: 40px; width: 620px; height: 438px;
    background: var(--paper); border: 2px solid var(--edge); border-radius: 3px;
    box-shadow: 0 2px 6px rgba(0,0,0,.12);
  }
  .spread-header {
    position: absolute; left: 0; right: 0; top: 0; height: 74px;
    background: var(--blue);
  }
  .spread-header .brand-name { position: absolute; left: 90px; top: 20px; font-size: 20px; }
  .spread-header .brand-sub { font-size: 9px; letter-spacing: 2px; margin-top: 3px; }
  .tagline {
    position: absolute; right: 90px; top: 32px;
    font-family: "Playfair Display", Georgia, serif; font-style: italic;
    font-size: 18px; color: var(--white);
  }
  .spread-footer {
    position: absolute; left: 0; right: 0; bottom: 0; height: 18px; background: var(--blue);
  }

  .menu-column { position: absolute; top: 84px; width: 180px; }
  .menu-column.left { left: 24px; }
  .menu-column.middle { left: 222px; }
  .menu-column.right { left: 420px; width: 176px; }

  .section-title {
    font-family: "Barlow Condensed", Arial, sans-serif; font-weight: 600;
    font-size: 13px; line-height: 15px; color: var(--blue);
    display: inline-block; padding: 0 14px 1px 3px;
    border-bottom: 1px solid var(--edge); border-left: 1px solid var(--edge);
    margin: 7px 0 4px;
  }
  .section-title:first-child { margin-top: 0; }
  .menu-list { list-style: none; }
  .menu-item {
    display: flex; justify-content: space-between; align-items: baseline;
    font-size: 8.5px; line-height: 11px;
  }
  .menu-item .price { flex: none; margin-left: 8px; }
  .item-note { display: block; font-style: italic; font-size: 7px; line-height: 8px; color: var(--note); }

  .heritage {
    display: flex; align-items: center; gap: 8px; margin-top: 10px;
  }
  .flags {
    width: 34px; height: 22px; border-radius: 2px; flex: none;
    background: linear-gradient(135deg, var(--blue) 0 50%, var(--red) 50% 100%);
  }
  .family-note {
    font-family: "Barlow Condensed", Arial, sans-serif; font-weight: 600;
    font-size: 10px; letter-spacing: .5px; color: var(--blue); text-transform: uppercase;
  }
  .disclaimer {
    margin-top: 8px;
    font-style: italic; font-size: 6.5px; line-height: 8px;
  }
</style>
</head>
<body>

  <section class="cover" aria-label="Menu cover">
    <div class="cover-band">
      <p class="brand-name">Brambleton<span class="brand-sub">Fish House</span></p>
      <p class="cover-label">menu</p>
    </div>
  </section>

  <section class="spread" aria-label="Menu inner spread">
    <header class="spread-header">
      <p class="brand-name">Brambleton<span class="brand-sub">Fish House</span></p>
      <p class="tagline">eat the fish</p>
    </header>

    <div class="menu-column left">
      <h2 class="section-title">Small Plates</h2>
      <ul class="menu-list">
        <li class="menu-item"><span>Sweet Thai Chili Calamari</span><span class="price">$00</span></li>
        <li class="menu-item"><span>Shrimp Stuffed Jalapeños</span><span class="price">$00</span></li>
        <li class="menu-item"><span>Hamachi Crudo</span><span class="price">$00</span></li>
        <li class="menu-item"><span>House Smoked Salmon<span class="item-note">Pemmick Crackers and Pickled Celery</span></span><span class="price">$00</span></li>
        <li class="menu-item"><span>Seared Teriyaki Tidbits</span><span class="price">$00</span></li>
        <li class="menu-item"><span>Sliders<span class="item-note">Crab Salad, Sausage &amp; Provolone, Mini Cheeseburgers</span></span><span class="price">$00</span></li>
        <li class="menu-item"><span>Fried Green Tomatoes<span class="item-note">Crab and Tarragon-Chive Aioli</span></span><span class="price">$00</span></li>
        <li class="menu-item"><span>Tomato Soup</span><span class="price">$00</span></li>
        <li class="menu-item"><span>Seafood Bisque</span><span class="price">$00</span></li>
        <li class="menu-item"><span>House Salad with Choice of Dressings</span><span class="price">$00</span></li>
        <li class="menu-item"><span>Small Caesar Salad</span><span class="price">$00</span></li>
      </ul>

      <h2 class="section-title">From the Sea</h2>
      <ul class="menu-list">
        <li class="menu-item"><span>Wood Grilled Black Smoked Salmon<span class="item-note">Sea Salt and Pepper</span></span><span class="price">$00</span></li>
        <li class="menu-item"><span>Miso Black Cod</span><span class="price">$00</span></li>
        <li class="menu-item"><span>Carta Fata White Fish</span><span class="price">$00</span></li>
        <li class="menu-item"><span>Whole Fish</span><span class="price">$00</span></li>
        <li class="menu-item"><span>Fish ’n Chips</span><span class="price">$00</span></li>
        <li class="menu-item"><span>Lobster</span><span class="price">$00</span></li>
        <li class="menu-item"><span>Steamed Clams and/or Mussels</span><span class="price">$00</span></li>
        <li class="menu-item"><span>Seared Scallops</span><span class="price">$00</span></li>
        <li class="menu-item"><span>Roasted Garlic Shrimp</span><span class="price">$00</span></li>
        <li class="menu-item"><span>Crab Cakes with Trio of Dipping Butters</span><span class="price">$00</span></li>
      </ul>
    </div>

    <div class="menu-column middle">
      <h2 class="section-title">From the Farm</h2>
      <ul class="menu-list">
        <li class="menu-item"><span>Caesar Salad Entree<span class="item-note">Choice of Chicken, Fish or Crab</span></span><span class="price">$00</span></li>
        <li class="menu-item"><span>Seafood Cobb</span><span class="price">$00</span></li>
        <li class="menu-item"><span>Caprese</span><span class="price">$00</span></li>
        <li class="menu-item"><span>Farmhouse</span><span class="price">$00</span></li>
      </ul>

      <h2 class="section-title">Snacks</h2>
      <ul class="menu-list">
        <li class="menu-item"><span>Fish Tacos</span><span class="price">$00</span></li>
        <li class="menu-item"><span>Rolls<span class="item-note">Lobster, Crab or Shrimp</span></span><span class="price">$00</span></li>
        <li class="menu-item"><span>Grilled Chicken Avocado and Bacon</span><span class="price">$00</span></li>
        <li class="menu-item"><span>Grilled Cheese with Tomato Soup</span><span class="price">$00</span></li>
      </ul>

      <h2 class="section-title">From the Ranch</h2>
      <ul class="menu-list">
        <li class="menu-item"><span>Wood Grilled 16 oz Rib Eye</span><span class="price">$00</span></li>
        <li class="menu-item"><span>Wood Grilled 10 oz Top Sirloin</span><span class="price">$00</span></li>
        <li class="menu-item"><span>Wood Grilled Half Chicken</span><span class="price">$00</span></li>
        <li class="menu-item"><span>Wood Grilled Pork Chop</span><span class="price">$00</span></li>
      </ul>
    </div>

    <div class="menu-column right">
      <h2 class="section-title">Desserts</h2>
      <ul class="menu-list">
        <li class="menu-item"><span>Key Lime Pie</span><span class="price">$00</span></li>
        <li class="menu-item"><span>Molted Chocolate Cake</span><span class="price">$00</span></li>
        <li class="menu-item"><span>Banana Fosters / Cherries Jubilee</span><span class="price">$00</span></li>
      </ul>

      <h2 class="section-title">Wine by the Bottle</h2>
      <ul class="menu-list">
        <li class="menu-item"><span>Chardonnay</span><span class="price">$00</span></li>
        <li class="menu-item"><span>Sauvignon Blanc</span><span class="price">$00</span></li>
        <li class="menu-item"><span>Riesling</span><span class="price">$00</span></li>
        <li class="menu-item"><span>Champagne</span><span class="price">$00</span></li>
        <li class="menu-item"><span>Interesting Whites</span><span class="price">$00</span></li>
        <li class="menu-item"><span>Pinot Noir</span><span class="price">$00</span></li>
        <li class="menu-item"><span>Merlot</span><span class="price">$00</span></li>
        <li class="menu-item"><span>Syrah</span><span class="price">$00</span></li>
        <li class="menu-item"><span>Cabernet Sauvignon</span><span class="price">$00</span></li>
        <li class="menu-item"><span>Interesting Reds</span><span class="price">$00</span></li>
      </ul>

      <div class="heritage">
        <div class="flags" role="img" aria-label="Crossed American and Canadian flags"></div>
        <p class="family-note">Family Owned &amp; Operated</p>
      </div>

      <p class="disclaimer">Disclaimer: All steaks and Burgers are cooked to order. Consuming raw, undercooked and unpasteurized food items may increase your chance of foodborne illnesses. We use nut and nut based oils in some of our menu items. If you are allergic to nuts or any other foods, please let us know.</p>
    </div>

    <div class="spread-footer"></div>
  </section>

</body>
</html>
```